Home Security Company Business Card

Looking for a eye catching business card that is non traditional and stands out but yet still looks professional. It should include all the pertinent information such as name, title, address, telephone, e-mail, website address should definitely stand out and then finally the logo.

Target Market(s)

Residential and Commercial accounts mostly upscale accounts

Industry/Entity Type

Security

Contact Information for Business Card

Name
Title
Address
Office #
Cell #
E-mail
Website

Font styles to use
Serif
Sans Serif

Requirements
Must have
• Logo, two sided color configuration
Nice to have
• You decide
Should not have
• There really aren't any.

```html
<!DOCTYPE html>
<html lang="en">
<head>
<meta charset="utf-8">
<title>Hearthwatch Security Systems Inc. – Business Card</title>
<link rel="stylesheet" href="https://fonts.googleapis.com/css2?family=Open+Sans:wght@400;600;700&display=swap">
<style>
  :root {
    --bg: #e9e4dc;
    --paper: #fbfbfa;
    --brand-red: #8e1b22;
    --text-dark: #3a3a3a;
    --text-grey: #8a8a8a;
    --shadow: rgba(40, 28, 14, 0.28);
  }
  * { margin: 0; padding: 0; box-sizing: border-box; }
  html, body {
    width: 1200px; height: 899px; overflow: hidden;
    background: var(--bg);
  }
  .stage { position: relative; width: 1200px; height: 899px; }
  .card {
    position: absolute; top: 150px;
    width: 340px; height: 595px;
    background: var(--paper);
    box-shadow: 0 10px 28px var(--shadow);
  }
  .card--back { left: 220px; }
  .card--front { left: 640px; }

  .brand {
    font-family: "Open Sans", sans-serif;
    font-weight: 600;
    font-size: 15px;
    color: var(--text-dark);
    display: flex; align-items: center; gap: 9px;
    white-space: nowrap;
    line-height: 1.2;
  }
  .brand__mark { width: 12px; height: 12px; background: var(--brand-red); flex: none; }

  .card--back .brand { position: absolute; left: 26px; top: 250px; }

  .back-footer {
    position: absolute; left: 0; right: 0; bottom: 62px;
    display: flex; align-items: center; justify-content: space-between;
  }
  .back-footer__bar { width: 32px; height: 10px; background: var(--brand-red); }
  .back-footer__web {
    font-family: "Open Sans", sans-serif;
    font-size: 13px; letter-spacing: 2.6px; color: var(--text-dark);
  }

  .card--front .brand { position: absolute; right: 20px; top: 110px; }

  .contact {
    position: absolute; left: 0; top: 236px; right: 24px;
    font-family: "Open Sans", sans-serif;
  }
  .contact__head { display: flex; align-items: flex-start; gap: 18px; }
  .contact__tab { width: 24px; height: 26px; background: var(--brand-red); margin-top: 2px; }
  .contact__name { font-size: 19px; font-weight: 700; color: var(--brand-red); line-height: 1.2; }
  .contact__title { font-size: 12px; color: var(--text-dark); }
  .contact__list { list-style: none; margin: 26px 0 0 42px; }
  .contact__list li {
    display: flex; align-items: center; gap: 10px;
    font-size: 14px; color: var(--text-dark); line-height: 24px;
  }
  .contact__list li.gap { margin-top: 10px; }
  .contact__list svg { width: 13px; height: 13px; flex: none; }
  .contact__web { font-weight: 600; }
  .contact__address {
    margin: 20px 0 0 42px; font-size: 14px; color: var(--text-grey); line-height: 20px;
  }
</style>
</head>
<body>
<main class="stage">

  <section class="card card--back" aria-label="Card back">
    <div class="brand">
      <span class="brand__mark"></span>
      <span class="brand__name">Hearthwatch Security Systems Inc.</span>
    </div>
    <div class="back-footer">
      <span class="back-footer__bar"></span>
      <span class="back-footer__web">www.hearthwatch.com</span>
      <span class="back-footer__bar"></span>
    </div>
  </section>

  <section class="card card--front" aria-label="Card front">
    <div class="brand">
      <span class="brand__mark"></span>
      <span class="brand__name">Hearthwatch Security Systems Inc.</span>
    </div>

    <div class="contact">
      <div class="contact__head">
        <span class="contact__tab"></span>
        <div>
          <div class="contact__name">Your Name</div>
          <div class="contact__title">Job Title Here</div>
        </div>
      </div>

      <ul class="contact__list">
        <li>
          <svg viewBox="0 0 14 14" aria-hidden="true"><path fill="#8e1b22" d="M3 1l2.2 2.6-1.2 1.6c.8 1.8 2.2 3.2 4 4l1.6-1.2L12.2 10 11 12.6C6 12.4 1.6 8 1.4 3z"/></svg>
          (555) 010 2030
        </li>
        <li>
          <svg viewBox="0 0 14 14" aria-hidden="true"><rect x="3.5" y="1" width="7" height="12" rx="1.2" fill="#8e1b22"/><rect x="5" y="2.6" width="4" height="7" fill="#fbfbfa"/></svg>
          083 555 0140
        </li>
        <li class="gap">
          <svg viewBox="0 0 14 14" aria-hidden="true"><rect x="1" y="3" width="12" height="8.5" fill="#8e1b22"/><path d="M1.5 3.5L7 8l5.5-4.5" stroke="#fbfbfa" stroke-width="1.1" fill="none"/></svg>
          yourmail@email.com
        </li>
        <li>
          <svg viewBox="0 0 14 14" aria-hidden="true"><circle cx="7" cy="7" r="6" fill="#8e1b22"/><path d="M1 7h12M7 1c-2.4 3-2.4 9 0 12M7 1c2.4 3 2.4 9 0 12" stroke="#fbfbfa" stroke-width="0.9" fill="none"/></svg>
          <span class="contact__web">www.hearthwatch.com</span>
        </li>
      </ul>

      <p class="contact__address">1234 address address address address<br>address address address</p>
    </div>
  </section>

</main>
</body>
</html>
```